Urgent * Legal Consultant Website Design

Provide a brief overview about your business Hello, website design required for independent legal consultant. Upload your company logo in the brief UPLOADED Specify the main navigation menu of your website (For better reference here's a sample of a website's navigation menu: (http://pixelrow.com/wp-content/uploads/2012/css-menu/ 3.jpg) Header menu should include: About Us, Our people, Services and Contact Us Indicate the subpages or the dropdown menu if you have any (Refer to: http://venmi.co/wp-content/uploads/2010 /11/nav.jpg) No Subpages in the dropdown Upload to separate file for the text or the content needed for the homepage (This is a helpful supporting file to provide in order for our designers to better understand the elements needed on how to layout your This could be in Word document if you're using Windows or in Pages if you are using Mac. ) GET your legal advice and protect you and your BUSINESS Family Law Debt Recovery Leases Crimes & Traffic, wills Violence Restraining Orders Probate Titles Shariah Law Provide some samples of Web designs you like for better reference (Cite 2 to 3 samples) Website must be clean , simple and display our services in a clear way. Examples: https://cdn.plinthora.com/wp/wp-content/uploads/sites/2/brisova-simple-business-wordpress-theme-1024x846.jpg https://cdn.plinthora.com/wp/wp -content / uploads / sites / 2 / corvelle-creative-studio-wp-website-template-1024x791.jpg Upload photos or files you would like to include in the design, or make mention if you are open to use stock photos Open to Use stock photos
Number of Pages Required
1 page

```html
<!DOCTYPE html>
<html lang="en">
<head>
<meta charset="utf-8">
<title>Lexmere Counsel</title>
<link href="https://fonts.googleapis.com/css2?family=Crimson+Text:wght@400;600;700&family=Open+Sans:wght@400;700&display=swap" rel="stylesheet">
<style>
:root{
  --ink:#111111;
  --text:#333333;
  --muted:#555555;
  --gold:#e3c15a;
  --band:#f4f4f4;
  --card:#f3f3f3;
  --field:#ffffff;
  --rule:#222222;
  --bottom:#e4e4e4;
  --hero-dark:#3a3a3a;
  --hero-light:#9a9a9a;
}
*{box-sizing:border-box;margin:0;padding:0}
html,body{width:1200px;height:3475px;overflow:hidden;background:#fff}
body{position:relative;font-family:"Crimson Text",Georgia,serif;color:var(--text)}
.abs{position:absolute}

/* header */
.site-header{position:absolute;left:0;top:0;width:1200px;height:132px;background:#fff}
.brand{position:absolute;left:139px;top:56px;font-size:26px;font-weight:700;color:var(--ink);letter-spacing:.5px}
.nav{position:absolute;top:64px;left:0;width:1200px;font-size:14px;color:var(--ink);letter-spacing:.5px}
.nav span{position:absolute;white-space:nowrap}
.nav .active{color:var(--gold)}
.nav .active::after{content:"";position:absolute;left:0;right:0;bottom:-6px;height:1px;background:var(--gold)}

/* hero */
.hero{position:absolute;left:0;top:132px;width:1200px;height:571px}
.hero-photo{position:absolute;inset:0;background:radial-gradient(ellipse at 55% 50%,var(--hero-light),var(--hero-dark) 75%)}
.hero-title{position:absolute;top:194px;width:1200px;text-align:center;color:#fff;font-size:38px;line-height:43px;font-weight:400}
.hero-sub{position:absolute;top:284px;width:1200px;text-align:center;color:#fff;font-size:15px}
.hero-btn{position:absolute;left:498px;top:318px;width:204px;height:36px;border:1.5px solid #fff;color:#fff;font-size:17px;font-weight:700;text-align:center;line-height:33px}

/* generic */
.heading{font-weight:700;color:var(--ink);font-size:21px;text-align:center;width:1200px;position:absolute;left:0}
.lede{font-size:14px;line-height:17px;color:var(--muted);text-align:center;width:1200px;position:absolute;left:0}
.btn-small{position:absolute;height:22px;border:1.5px solid var(--rule);font-size:12px;font-weight:700;color:var(--ink);text-align:center;line-height:19px}
.band{position:absolute;left:0;width:1200px;background:var(--band)}

/* about */
.portrait{position:absolute;left:208px;top:897px;width:197px;height:333px;background:linear-gradient(180deg,#bdbdbd,#3c3c3c)}
.about-title{position:absolute;left:462px;top:1005px;font-size:21px;font-weight:700;color:var(--ink)}
.about-text{position:absolute;left:462px;top:1040px;width:522px;font-size:14px;line-height:18px;color:var(--muted)}

/* practice */
.card{position:absolute;width:220px;height:224px;background:var(--card)}
.card svg{position:absolute;left:88px;top:60px}
.card-label{position:absolute;left:0;top:132px;width:220px;text-align:center;font-size:16px;color:var(--ink)}

/* form */
.field{position:absolute;height:25px;background:var(--field);font-size:11px;color:var(--ink);padding:5px 10px}
.field svg{position:absolute;right:10px;top:9px}

/* people */
.person-photo{position:absolute;top:2448px;width:285px;height:285px;background:linear-gradient(180deg,#cfcfcf,#5a5a5a)}
.person-name{position:absolute;top:2755px;width:285px;text-align:center;font-size:17px;color:var(--ink)}
.person-role{position:absolute;top:2777px;width:285px;text-align:center;font-size:13px;color:var(--muted)}

/* testimonials */
.quote{position:absolute;top:2982px;width:260px;font-size:12px;line-height:15px;color:var(--muted)}
.quote-mark{position:absolute;font-size:48px;color:#bbbbbb;line-height:1}
.quote-name{font-family:"Open Sans",Arial,sans-serif;font-weight:700;font-size:12px;color:var(--ink);margin-top:2px}

/* footer */
.foot-brand{position:absolute;left:136px;top:3185px;font-size:23px;font-weight:700;color:var(--ink)}
.foot-title{position:absolute;top:3226px;font-size:19px;font-weight:600;color:var(--ink)}
.foot-title::after{content:"";position:absolute;left:0;bottom:-6px;width:50px;height:1px;background:var(--rule)}
.foot-text{position:absolute;top:3262px;font-size:12px;line-height:15px;color:var(--muted)}
.links li{list-style:none;font-size:13px;line-height:24px;color:var(--muted)}
.links li::before{content:"›";margin-right:6px;color:var(--ink)}
.bottom-bar{position:absolute;left:0;top:3415px;width:1200px;height:60px;background:var(--bottom)}
.copyright{position:absolute;left:136px;top:21px;font-size:13px;color:var(--ink)}
.social{position:absolute;left:960px;top:24px;display:flex;gap:10px}
.social i{display:block;width:13px;height:13px;background:var(--ink);border-radius:50%}
</style>
</head>
<body>

<header class="site-header">
  <div class="brand">LEXMERE COUNSEL</div>
  <nav class="nav">
    <span class="active" style="left:512px">HOME</span>
    <span style="left:607px">ABOUT US</span>
    <span style="left:727px">OUR PEOPLE</span>
    <span style="left:862px">SERVICES</span>
    <span style="left:980px">CONTACT US</span>
  </nav>
</header>

<section class="hero">
  <div class="hero-photo" role="img" aria-label="Black and white photo of a lawyer and client shaking hands across a desk"></div>
  <h1 class="hero-title">Get Your Legal Advice<br>Protect You &amp; Your Business</h1>
  <p class="hero-sub">Business Law | Civil &amp; Commercial | Trust, Wills &amp; Probate</p>
  <div class="hero-btn">Free Legal Consultation</div>
</section>

<section>
  <h2 class="heading" style="top:773px">WELCOME TO LEXMERE COUNSEL</h2>
  <p class="lede" style="top:808px;left:350px;width:500px">Varietates autem iniurasque fortunae facile veterem philosophorum praecepta instituta vita etiam vehementer earum esse? Tu enim ista lenius, hic Stoicorum more nos vexat. Collatio igitur ista te nihil iuvat. Videamus animi partes, quarum est conspectus illustrior.</p>
  <div class="btn-small" style="left:560px;top:872px;width:80px">Read More</div>
</section>

<div class="band" style="top:955px;height:275px"></div>
<div class="portrait" role="img" aria-label="Portrait of a lawyer in a dark suit with arms crossed"></div>
<section>
  <h2 class="about-title">ABOUT US</h2>
  <p class="about-text">Lorem ipsum dolor sit amet, consectetur adipiscing elit. Quid autem habent admirationis, cum prope accesseris? An hoc usque quaque, aliter in vita? Non igitur de improbo, sed de callido improbo quaerimus, qualis Q. Nam quibus rebus efficiuntur voluptates, eae non sunt in potestate sapientis. Negare non possum. Quid iudicant sensus? Quibus ego vehementer assentior, quid vero propter Epicurum esse, si probatum, quae ille dicerent.</p>
  <div class="btn-small" style="left:462px;top:1160px;width:80px">Read More</div>
</section>

<section>
  <h2 class="heading" style="top:1265px">Practice Areas</h2>
  <p class="lede" style="top:1294px">Lorem ipsum dolor sit amet, consectetur adipiscing elit.<br>Quid autem habent admirationis,</p>

  <div class="card" style="left:139px;top:1362px">
    <svg width="44" height="44" viewBox="0 0 44 44" fill="none" stroke="#111" stroke-width="3"><path d="M6 22 22 8l16 14"/><path d="M11 19v18h22V19"/><rect x="18" y="26" width="8" height="11" fill="#111"/></svg>
    <div class="card-label">Family Law</div>
  </div>
  <div class="card" style="left:373px;top:1362px">
    <svg width="44" height="44" viewBox="0 0 44 44" fill="none" stroke="#111" stroke-width="2.5"><circle cx="22" cy="22" r="17"/><text x="22" y="30" text-anchor="middle" font-size="22" font-family="Georgia,serif" fill="#111" stroke="none" font-weight="700">$</text></svg>
    <div class="card-label">Debt Recovery</div>
  </div>
  <div class="card" style="left:607px;top:1362px">
    <svg width="44" height="44" viewBox="0 0 44 44" fill="none" stroke="#111" stroke-width="2.5"><rect x="8" y="6" width="20" height="26"/><path d="M13 13h10M13 19h10"/><circle cx="30" cy="32" r="5" fill="#111"/><path d="M30 37v5"/></svg>
    <div class="card-label">Leases</div>
  </div>
  <div class="card" style="left:841px;top:1362px">
    <svg width="44" height="44" viewBox="0 0 44 44" fill="none" stroke="#111" stroke-width="2.5"><path d="M22 5 36 10v12c0 9-6 15-14 18C14 37 8 31 8 22V10z"/><path d="M16 22l5 5 8-10"/></svg>
    <div class="card-label">Crimes &amp; Traffic</div>
  </div>

  <div class="card" style="left:139px;top:1600px">
    <svg width="44" height="44" viewBox="0 0 44 44" fill="none" stroke="#111" stroke-width="2.5"><rect x="10" y="5" width="24" height="34"/><path d="M15 13h14M15 19h14M15 25h14M15 31h9"/></svg>
    <div class="card-label">Wills</div>
  </div>
  <div class="card" style="left:373px;top:1600px">
    <svg width="44" height="44" viewBox="0 0 44 44" fill="none" stroke="#111" stroke-width="3"><path d="M8 8l26 26M36 8 10 34"/><path d="M30 38l8-8M6 30l8 8"/></svg>
    <div class="card-label">Violence</div>
  </div>
  <div class="card" style="left:607px;top:1600px">
    <svg width="44" height="44" viewBox="0 0 44 44" fill="none" stroke="#111" stroke-width="2.5"><rect x="7" y="6" width="24" height="32"/><path d="M12 14h13M12 20h13M12 26h8"/><path d="M38 12 24 32l-2 5 5-2 14-20z" fill="#111"/></svg>
    <div class="card-label">Probate Titles</div>
  </div>
  <div class="card" style="left:841px;top:1600px">
    <svg width="44" height="44" viewBox="0 0 44 44"><path d="M26 8a15 15 0 1 0 12 24A12 12 0 1 1 26 8z" fill="#111"/><path d="M19 6l1.5 4 4 .3-3 2.6 1 4-3.5-2.2-3.5 2.2 1-4-3-2.6 4-.3z" fill="#111"/></svg>
    <div class="card-label">Shariah Law</div>
  </div>
</section>

<div class="band" style="top:1884px;height:428px"></div>
<section>
  <h2 class="heading" style="top:1927px">Request a Free Consultation</h2>
  <p class="lede" style="top:1954px">Lorem ipsum dolor sit amet, consectetur adipiscing elit.<br>Quid autem habent admirationis,</p>
  <div class="field" style="left:166px;top:2028px;width:271px">Name</div>
  <div class="field" style="left:462px;top:2028px;width:271px">Phone</div>
  <div class="field" style="left:758px;top:2028px;width:271px">Family Law
    <svg width="10" height="7" viewBox="0 0 10 7"><path d="M0 0h10L5 7z" fill="#111"/></svg>
  </div>
  <div class="field" style="left:166px;top:2076px;width:863px;height:127px">Case Description..</div>
  <div class="btn-small" style="left:546px;top:2229px;width:104px;height:24px;font-weight:400;line-height:21px">Send Message</div>
</section>

<section>
  <h2 class="heading" style="top:2352px">Our people</h2>
  <p class="lede" style="top:2380px">Lorem ipsum dolor sit amet, consectetur adipiscing elit.<br>Quid autem habent admirationis,</p>
  <div class="person-photo" style="left:139px" role="img" aria-label="Portrait of an arbitrator in a light blouse"></div>
  <div class="person-photo" style="left:455px" role="img" aria-label="Portrait of the managing partner in a suit"></div>
  <div class="person-photo" style="left:772px" role="img" aria-label="Portrait of a counsel in a dark blazer"></div>
  <div class="person-name" style="left:139px">Clara Wendell</div>
  <div class="person-role" style="left:139px">Chartered Arbitrator</div>
  <div class="person-name" style="left:455px">Owen Radcliffe</div>
  <div class="person-role" style="left:455px">Managing Partner,Attorney</div>
  <div class="person-name" style="left:772px">Helen Marsh</div>
  <div class="person-role" style="left:772px">Counsel</div>
</section>

<div class="band" style="top:2867px;height:268px"></div>
<section>
  <h2 class="heading" style="top:2905px">Testimonials</h2>
  <svg class="abs" style="left:140px;top:2990px" width="22" height="42" viewBox="0 0 22 42" fill="none" stroke="#bbb" stroke-width="2"><path d="M20 1 2 21l18 20"/></svg>
  <svg class="abs" style="left:1038px;top:2990px" width="22" height="42" viewBox="0 0 22 42" fill="none" stroke="#bbb" stroke-width="2"><path d="M2 1l18 20L2 41"/></svg>

  <span class="quote-mark" style="left:290px;top:2968px">“</span>
  <div class="quote" style="left:314px">Lorem ipsum dolor sit amet, consectetur adipiscing elit. Quid autem habent admirationis,
    <div class="quote-name">Peter Lowe</div></div>
  <span class="quote-mark" style="left:532px;top:2995px">”</span>

  <span class="quote-mark" style="left:638px;top:2968px">“</span>
  <div class="quote" style="left:662px">Lorem ipsum dolor sit amet, consectetur adipiscing elit. Quid autem habent admirationis,
    <div class="quote-name">Simon Hale</div></div>
  <span class="quote-mark" style="left:880px;top:2995px">”</span>
</section>

<footer>
  <div class="foot-brand">LEXMERE COUNSEL</div>

  <h3 class="foot-title" style="left:136px">About Us</h3>
  <p class="foot-text" style="left:136px;width:240px">Lorem ipsum dolor sit amet, consectetur adipiscing elit. Quid autem habent admirationis, desperationem sapientiae, illi propter opum vivere. Quid enim me prohiberet Epicureum esse, si probarem?</p>
  <div class="btn-small" style="left:136px;top:3345px;width:156px;height:24px;line-height:21px">Free Legal Consultation</div>

  <h3 class="foot-title" style="left:485px">Quick Links</h3>
  <ul class="links abs" style="left:485px;top:3256px">
    <li>Home</li><li>About Us</li><li>Services</li><li>Our People</li><li>Contact Us</li>
  </ul>

  <h3 class="foot-title" style="left:689px">Contact Us</h3>
  <p class="foot-text" style="left:689px;width:200px;line-height:16px">742 Alder Row<br>Brookfield Vale, 40217<br><br>P. 555-014-2208<br>C. 555-017-3391<br>hello@lexmerecounsel.example<br>www.lexmerecounsel.example</p>

  <h3 class="foot-title" style="left:902px">News Letter</h3>
  <p class="foot-text" style="left:902px;width:170px">Lorem ipsum dolor sit amet, consectetur adipiscing elit.</p>
  <div class="field abs" style="left:902px;top:3308px;width:158px;height:30px;border:1px solid #999;font-size:10px;color:#888;text-align:center;padding-top:8px">Your Email Address</div>
  <div class="abs" style="left:902px;top:3345px;width:158px;height:30px;background:var(--ink);color:#fff;font-size:10px;text-align:center;line-height:30px;letter-spacing:.5px">SUBSCRIBE</div>

  <div class="bottom-bar">
    <div class="copyright">© 2018 Lexmere Counsel &nbsp;|&nbsp; Privacy Policy &nbsp;|&nbsp; User Agreement</div>
    <div class="social" aria-label="Social links"><i></i><i></i><i></i><i></i><i></i></div>
  </div>
</footer>

</body>
</html>
```